Website for New Business in Luxury Home Market

Build a website for a new business that is an off shoot of my primary business as an interior designer. These days, with Brimlo, QRMK and print media telling people they can be their own interior designer, General Contractors building a new home or remodeling, are frustrated because they do not get the information they need to be able to build or remodel. Clients/owners are often unaware that picking the pretty things like faucets, tile or appliances require specifications and drawings to tell the individual sub contractors how to proceed with their work, or to bid the project correctly. The professional interior designer used to fill this gap. Even if there is an architect on the project, many architects do not issue an ID Set (Interior Design Set). To fill this gap, we have started Varnell Detail Group. Although we are interior designers, we will provide only specification services. By interfacing with the client and contractor, we will provide the client with a schedule and prompt them when it is time to shop. Additionally, we will give them a list of GC preferred vendors for them to shop with. Once selections have been made, specifications will be written, plans will be tagged. This process continues for all the pieces necessary for a home to be built: Plumbing, Appliances, Mouldings, Interior Doors, Cabinets, Hard Surfaces (Including counters, and showers), Flooring, Motorized Window Coverings, Hardware, Room Finish Schedule, Lighting - Recessed, Decorative and Exterior, Electrical Outlets, Exterior Hardscape Materials.

Professional contractors are used to receiving this information. Without the interior designer, the contractor often has to step in to guide the client. This takes him or her away from their actual job of building the house. What this translates to is a project that becomes late and over budget. The cost benefit of the specification process is that the project can be delivered on time, and helps to control the budget. By delivering on time, the homeowner does not incur additional interest charges and other costs involved in construction delays.

I would like a website that is built on a platform that I can edit if I need to do so, without having to call someone else to do it. Perhaps on Wix or Square Space if this is possible. I would like the ability to link social media. Also, if the photos need changing, it should be something simple for me to do. The website should be relatively simple. Show a few photos of the finished product along with the drawings that led up to them. I would also like to show a project spec sheet.

I've uploaded the photos and some of the documentation. The documentation will be a placeholder for the moment. I will change them to reflect the new logo and change the clients name. These will be ready next week, but for now we can use what I'm providing.

I like the "background' squiggle on my logo. Perhaps this can be integrated in some way. The website should tell in a concise manner what we do and who we do it for. It should appeal to the General Contractor, but could also be directed to the homeowner. I have lots of other photos if more are needed, but these are a start. I think too much info on the website won't help.

Target Market(s)

Luxury Home Builders; Professional General Contractors, People building luxury homes or remodeling a luxury property who don't want to use an interior designer.

Industry/Entity Type

Business

Coding

Coded - Design and coding required

Number of Pages Required

4 page

Font styles to use
Other font styles liked:
• Use fonts that work with the logo I sent

Colors
ec1f27
c3c3c3

Requirements
Must have
• Company Name and Logo, About, Contact Us, FAQ, Photos and Specs. Use the files I sent for the Logo, and the colors for the website should be derived from those files. I like clean and simple.
Nice to have
• Builder Testimonials. I am working on getting two.
Should not have
• Not sure until I see it.

```html
<!DOCTYPE html>
<html lang="en">
<head>
<meta charset="utf-8">
<title>Varnell Detail Group — Home Renovation</title>
<link href="https://fonts.googleapis.com/css2?family=Poppins:wght@300;400;500;600&family=Open+Sans:wght@400&display=swap" rel="stylesheet">
<style>
:root{
  --red:#ec1f27;
  --red-deep:#5a0d10;
  --grey:#c3c3c3;
  --ink:#222;
  --text:#555;
  --muted:#8a8a8a;
  --dark:#222;
  --darker:#1b1b1b;
  --band:#2b2b2b;
  --white:#fff;
  --line:#e4e4e4;
}
*{box-sizing:border-box;margin:0;padding:0}
html,body{width:1200px;height:3390px;overflow:hidden}
body{font-family:"Poppins",sans-serif;color:var(--text);background:var(--white);position:relative}
section,header,footer{position:absolute;left:0;width:1200px}
.wrap{position:relative;width:974px;margin:0 auto;height:100%}

/* top bar */
.topbar{top:0;height:40px;background:#f4f4f4;border-bottom:1px solid var(--line)}
.topbar .tagline{position:absolute;left:0;top:12px;font-size:11px;color:var(--muted)}
.topbar .office{position:absolute;left:700px;top:11px;font-size:12px;color:var(--ink)}
.topbar .office svg{vertical-align:-2px;margin-right:5px}
.social{position:absolute;display:flex;gap:18px}
.topbar .social{right:0;top:14px}
.social span{width:12px;height:12px;border-radius:50%;border:1.5px solid var(--muted);display:block}

/* nav */
.nav{top:40px;height:112px;background:var(--white)}
.brand{position:absolute;display:flex;align-items:center;gap:10px}
.nav .brand{left:0;top:34px}
.brand .mark{width:30px;height:30px;background:var(--red-deep);display:block}
.brand .name{font-size:15px;font-weight:400;color:#555;line-height:1.1;width:130px}
.menu{position:absolute;right:0;top:46px;display:flex;gap:38px;list-style:none;font-size:13px;color:var(--ink)}

/* hero */
.hero{top:152px;height:498px;background:radial-gradient(ellipse at 55% 35%,#6a4a30 0%,#3b2a1c 45%,#1e150e 100%)}
.hero .shade{position:absolute;inset:0;background:rgba(0,0,0,.25)}
.hero h1{position:absolute;top:80px;width:100%;text-align:center;color:var(--white);font-weight:300;font-size:72px;line-height:84px}
.hero h1 b{display:block;font-weight:600}
.hero p{position:absolute;top:258px;left:240px;width:720px;text-align:center;color:var(--white);font-size:21px;line-height:29px;font-weight:400}

/* section titles */
.title{position:absolute;width:100%;text-align:center;font-size:40px;font-weight:300;color:var(--ink)}
.title b{font-weight:600}
.lead{position:absolute;width:100%;text-align:center;font-size:11.5px;line-height:22px;color:var(--ink)}

/* services */
.services{top:650px;height:627px}
.services .title{top:58px}
.services .lead{top:116px;left:0}
.svc{position:absolute;width:310px;text-align:center}
.svc svg{display:block;margin:0 auto 8px}
.svc h3{font-size:16px;font-weight:400;color:var(--ink);margin-bottom:10px}
.svc p{font-size:11.5px;line-height:22px;color:var(--ink)}

/* specs */
.specs{top:1277px;height:463px}
.specs .drawing{position:absolute;left:0;top:18px;width:532px;height:420px;background:linear-gradient(135deg,#f6f6f6,#e9e9e9)}
.specs h2{position:absolute;left:554px;top:18px;font-size:34px;line-height:50px;font-weight:400;color:var(--ink)}
.specs h2 b{font-weight:600}
.spec-row{position:absolute;left:554px;width:533px;display:flex;gap:56px}
.spec-row .thumb{width:86px;flex:none}
.spec-row p{font-size:11.5px;line-height:22px;color:var(--ink)}

/* projects */
.projects{top:1740px;height:540px}
.projects .title{top:55px}
.projects .lead{top:112px}
.grid{position:absolute;left:113px;top:158px;width:974px;height:358px;display:grid;grid-template-columns:repeat(4,1fr);grid-template-rows:repeat(2,1fr)}
.tile{position:relative;text-align:center;color:var(--white)}
.tile h4{font-size:17px;font-weight:400;margin:46px 0 10px}
.tile p{font-size:11.5px;line-height:22px;padding:0 40px}
.tile.red{background:var(--red)}
.tile.fade{background:#3a0b0d;color:rgba(255,255,255,.18)}
.tile.photo-dark{background:linear-gradient(160deg,#2a2320,#0f0c0b)}
.tile.photo-warm{background:linear-gradient(160deg,#6b5540,#2c2118)}
.tile.photo-dusk{background:linear-gradient(180deg,#5c7285,#2d2a24)}
.tile.photo-night{background:linear-gradient(180deg,#4a3a2c,#1f1812)}
.btn-ghost{position:absolute;left:47px;top:72px;width:150px;height:36px;border:1px solid var(--white);color:var(--white);font-size:11px;line-height:34px;letter-spacing:.5px}

/* service tabs */
.tabs{top:2305px;height:389px}
.tabs .band{position:absolute;left:0;top:174px;width:1200px;height:177px;background:var(--band)}
.tab-list{position:absolute;left:113px;top:0;list-style:none}
.tab-list li{position:relative;width:249px;height:62px;margin-bottom:8px;display:flex;align-items:center;gap:20px;padding-left:70px;font-size:13px;color:var(--ink);background:var(--white);border:1px solid var(--line);clip-path:polygon(40px 0,100% 0,100% 100%,0 100%)}
.tab-list li svg{flex:none}
.panel{position:absolute;left:362px;top:0;width:366px;height:389px;background:var(--white);border:1px solid var(--line);clip-path:polygon(0 0,100% 0,100% 100%,0 100%,0 80%,-20px 50%,0 20%)}
.panel .sketch{position:absolute;left:27px;top:23px;width:311px;height:169px;background:linear-gradient(135deg,#f5f5f5,#e6e6e6);border:1px solid var(--line)}
.panel h4{position:absolute;left:27px;top:212px;font-size:13px;font-weight:600;color:var(--red)}
.panel p{position:absolute;left:27px;top:240px;width:315px;font-size:11.5px;line-height:22px;color:var(--ink)}
.tabs .feature{position:absolute;left:728px;top:0;width:359px;height:389px;background:linear-gradient(180deg,#3b4a5c 0%,#6b5a45 55%,#2c241c 100%)}

/* testimonial */
.testimonial{top:2694px;height:402px}
.avatar{position:absolute;left:533px;top:63px;width:150px;height:150px;border-radius:50%;background:radial-gradient(circle at 50% 40%,#b59a84,#5a4a40);border:4px solid var(--white);box-shadow:0 0 0 1px var(--line)}
.quote{position:absolute;left:192px;top:223px;width:816px;text-align:center;font-family:"Open Sans",sans-serif;font-size:11px;line-height:22px;color:#666}
.dots{position:absolute;left:561px;top:327px;display:flex;gap:9px}
.dots span{width:12px;height:12px;border-radius:50%;background:var(--grey)}
.dots span.on{background:var(--red)}

/* footer */
.footer{top:3096px;height:244px;background:var(--dark);color:var(--white)}
.footer .brand{left:0;top:46px}
.footer .brand .name{color:#ddd}
.footer .about{position:absolute;left:0;top:136px;width:280px;font-size:11.5px;line-height:22px}
.footer h5{font-size:16px;font-weight:500;margin-bottom:12px}
.col{position:absolute;top:48px}
.col p{font-size:11.5px;line-height:22px}
.col .mail{color:var(--red)}
.col dl{display:grid;grid-template-columns:60px auto;font-size:12px;line-height:22px}
.col dd{font-weight:600}
.newsletter{left:689px;width:285px}
.field{width:285px;height:39px;background:#333;border:1px solid #3a3a3a;font-size:10.5px;color:#999;padding:12px 14px;margin-top:6px}
.subscribe{width:118px;height:39px;margin-top:13px;background:var(--red);font-size:11.5px;text-align:center;line-height:39px;letter-spacing:.5px}
.legal{top:3340px;height:50px;background:var(--darker)}
.legal .social{left:0;top:19px}
.legal .social span{border-color:#777}
.legal small{position:absolute;right:0;top:17px;font-size:10.5px;color:#888}
</style>
</head>
<body>

<header class="topbar">
  <div class="wrap">
    <p class="tagline">Hire us to turn your property around and make it stand out!</p>
    <p class="office"><svg width="12" height="12" viewBox="0 0 24 24"><path fill="#ec1f27" d="M6.6 10.8a15.1 15.1 0 006.6 6.6l2.2-2.2a1 1 0 011-.25 11.4 11.4 0 003.6.6 1 1 0 011 1V20a1 1 0 01-1 1A17 17 0 013 4a1 1 0 011-1h3.5a1 1 0 011 1 11.4 11.4 0 00.6 3.6 1 1 0 01-.25 1z"/></svg><b>Office:</b> 555.204.7713</p>
    <div class="social" aria-label="Social links"><span></span><span></span><span></span></div>
  </div>
</header>

<header class="nav">
  <div class="wrap">
    <div class="brand"><span class="mark"></span><span class="name">Varnell Detail Group</span></div>
    <ul class="menu">
      <li>About</li><li>Services</li><li>Photos</li><li>FAQ</li><li>Specs</li><li>Testimonials</li><li>Contact us</li>
    </ul>
  </div>
</header>

<section class="hero" role="img" aria-label="Photo of a luxury kitchen interior with dark wood cabinetry and a chandelier">
  <div class="shade"></div>
  <h1>Home <b>Renovation</b></h1>
  <p>Sorem ipsum dolor sit amet, consectetuer adipiscing elit, sed diam nonummy nibh euismod tinciilaoreet magna aliquamerat volutpat. Ut wisi enim ad minim.</p>
</section>

<section class="services">
  <h2 class="title">Our <b>Services</b></h2>
  <p class="lead" style="left:113px;width:974px">Sorem ipsum dolor sit amet, consectetuer adipiscing elit, sed diam nonummy nibh euismod tinciilaoreet magna aliquamerat volutpat. Ut wisi enim ad minim. Sorem ipsum dolor sit amet, consectetuer adipiscing elit, sed diam nonummy nibh euismod tinciilaoreet .</p>

  <div class="svc" style="left:110px;top:200px">
    <svg width="44" height="44" viewBox="0 0 44 44" fill="none" stroke="#ec1f27" stroke-width="2"><path d="M4 20L22 6l18 14"/><rect x="9" y="18" width="26" height="22"/><rect x="18" y="28" width="8" height="12"/></svg>
    <h3>Home Remodeling</h3>
    <p>Sorem ipsum dolor sit amet, consectetu adipiscing elit, sed diam nonummy nibh euismod tinciilaoreet magna aliquamerat volutpat. Ut wisi enim ad minim. Sorem ipsum dolor.</p>
  </div>
  <div class="svc" style="left:445px;top:200px">
    <svg width="44" height="44" viewBox="0 0 44 44" fill="none" stroke="#ec1f27" stroke-width="2"><path d="M6 40V6l34 34z"/><path d="M14 32V22l10 10z"/><path d="M6 14h5M6 22h5M6 30h5"/></svg>
    <h3>New Home Construction</h3>
    <p>Sorem ipsum dolor sit amet, consectetu adipiscing elit, sed diam nonummy nibh euismod tinciilaoreet magna aliquamerat volutpat. Ut wisi enim ad minim. Sorem ipsum dolor.</p>
  </div>
  <div class="svc" style="left:778px;top:200px">
    <svg width="44" height="44" viewBox="0 0 44 44" fill="none" stroke="#ec1f27" stroke-width="2"><rect x="10" y="4" width="24" height="36"/><rect x="15" y="9" width="14" height="12"/><circle cx="28" cy="26" r="1.5"/><path d="M4 40h36"/></svg>
    <h3>Exterior Renovation</h3>
    <p>Sorem ipsum dolor sit amet, consectetu adipiscing elit, sed diam nonummy nibh euismod tinciilaoreet magna aliquamerat volutpat. Ut wisi enim ad minim. Sorem ipsum dolor.</p>
  </div>
  <div class="svc" style="left:110px;top:418px">
    <svg width="44" height="44" viewBox="0 0 44 44" fill="none" stroke="#ec1f27" stroke-width="2"><rect x="4" y="8" width="36" height="28"/><path d="M4 17h36M4 27h36M16 8v9M28 17v10M16 27v9"/></svg>
    <h3>Hardscapes</h3>
    <p>Sorem ipsum dolor sit amet, consectetu adipiscing elit, sed diam nonummy nibh euismod tinciilaoreet magna aliquamerat volutpat. Ut wisi enim ad minim. Sorem ipsum dolor.</p>
  </div>
  <div class="svc" style="left:445px;top:418px">
    <svg width="44" height="44" viewBox="0 0 44 44" fill="none" stroke="#ec1f27" stroke-width="2"><path d="M22 4v8M16 12h12"/><path d="M4 20h36a18 14 0 01-36 0z"/><path d="M18 34v6h8v-6"/></svg>
    <h3>Bathroom Remodeling</h3>
    <p>Sorem ipsum dolor sit amet, consectetu adipiscing elit, sed diam nonummy nibh euismod tinciilaoreet magna aliquamerat volutpat. Ut wisi enim ad minim. Sorem ipsum dolor.</p>
  </div>
  <div class="svc" style="left:778px;top:418px">
    <svg width="44" height="44" viewBox="0 0 44 44" fill="none" stroke="#ec1f27" stroke-width="2"><rect x="10" y="4" width="24" height="36"/><path d="M10 16h24M10 28h24"/><path d="M20 10h4M20 22h4M20 34h4"/></svg>
    <h3>Kitchen Remodeling</h3>
    <p>Sorem ipsum dolor sit amet, consectetu adipiscing elit, sed diam nonummy nibh euismod tinciilaoreet magna aliquamerat volutpat. Ut wisi enim ad minim. Sorem ipsum dolor.</p>
  </div>
</section>

<section class="specs">
  <div class="drawing" role="img" aria-label="Architectural elevation drawing of bathroom and shower walls with tile grids and dimension callouts"></div>
  <h2>Sorem Ipsumam <b>Consectetuer Adipiscing Elit</b></h2>
  <div class="spec-row" style="top:124px">
    <div class="thumb" role="img" aria-label="3D floor plan render" style="height:91px;background:linear-gradient(135deg,#d9cfc3,#8f8275)"></div>
    <p>Sorem ipsum dolor sit amet, consectetuer adipiscing elit, sed diam nonummy nibh euismod tinciilaoreet magna aliquamerat volutpat. Ut wisi enim ad minim. Sorem ipsum dolor sit amet, consectetuer adipiscing elit, sed diam nonummy nibh euismod tinciilaoreet .</p>
  </div>
  <div class="spec-row" style="top:230px">
    <div class="thumb" role="img" aria-label="Tile elevation drawing" style="height:86px;background:linear-gradient(135deg,#f2f2f2,#d6d6d6)"></div>
    <p>Lorem ipsum dolor sit amet, consectetuer adipiscing elit, sed diam nonummy nibh euismod tinciilaoreet magna aliquamerat volutpat. Ut wisi enim ad minim. Sorem ipsum dolor sit amet, consectetuer adipiscing elit, sed diam nonummy nibh euismod tinciilaoreet .</p>
  </div>
  <div class="spec-row" style="top:334px">
    <div class="thumb" role="img" aria-label="Photo of a finished shower" style="height:118px;background:linear-gradient(180deg,#b9ad9e,#6d6255)"></div>
    <p>Worem ipsum dolor sit amet, consectetuer adipiscing elit, sed diam nonummy nibh euismod tinciilaoreet magna aliquamerat volutpat. Ut wisi enim ad minim. Sorem ipsum dolor sit amet, consectetuer adipiscing elit, sed diam nonummy nibh euismod tinciilaoreet .</p>
  </div>
</section>

<section class="projects">
  <h2 class="title">Our <b>Projects</b></h2>
  <p class="lead">Sorem ipsum dolor sit amet, consectetuer adipiscing elit, sed diam nonummy nibh euismod tinciilaoreet magna aliquamerat volutpat.</p>
  <div class="grid">
    <div class="tile photo-dark" role="img" aria-label="Photo of a dim luxury hallway"><span class="btn-ghost">VIEW DETAILS</span></div>
    <div class="tile fade"><h4>Project One</h4><p>Sorem ipsum dolor sit, consectetu adipiscing elit, sed diam nonummy nibh euismod tinciilaoreet.</p></div>
    <div class="tile photo-warm" role="img" aria-label="Photo of a patio dining area with palms"></div>
    <div class="tile red"><h4>Project One</h4><p>Sorem ipsum dolor sit, consectetu adipiscing elit, sed diam nonummy nibh euismod tinciilaoreet.</p></div>
    <div class="tile red"><h4>Project One</h4><p>Sorem ipsum dolor sit, consectetu adipiscing elit, sed diam nonummy nibh euismod tinciilaoreet.</p></div>
    <div class="tile photo-dusk" role="img" aria-label="Photo of an entry doorway opening to a lake view"></div>
    <div class="tile red"><h4>Project One</h4><p>Sorem ipsum dolor sit, consectetu adipiscing elit, sed diam nonummy nibh euismod tinciilaoreet.</p></div>
    <div class="tile photo-night" role="img" aria-label="Photo of a home exterior at night"></div>
  </div>
</section>

<section class="tabs">
  <div class="band"></div>
  <ul class="tab-list">
    <li><svg width="22" height="18" viewBox="0 0 22 18" fill="none" stroke="#666" stroke-width="1.5"><rect x="1" y="1" width="20" height="16"/><path d="M1 9h10V1"/></svg>RENOVATION</li>
    <li><svg width="20" height="20" viewBox="0 0 20 20" fill="none" stroke="#666" stroke-width="2"><path d="M2 2l16 16M18 2L2 18"/></svg>ARCHITECH</li>
    <li><svg width="22" height="18" viewBox="0 0 22 18" fill="none" stroke="#666" stroke-width="1.5"><path d="M1 17V7l10-6 10 6v10z"/><path d="M1 12h20M6 7v10M11 7v10M16 7v10"/></svg>ROOFING</li>
    <li><svg width="20" height="20" viewBox="0 0 20 20" fill="#666"><path d="M12 1l7 7-5 5-7-7z"/><path d="M8 9l3 3-8 7-2-2z"/></svg>PAINTING</li>
  </ul>
  <div class="panel">
    <div class="sketch" role="img" aria-label="Cabinet elevation drawing"></div>
    <h4>ARCHITECH</h4>
    <p>Worem ipsum dolor sit amet, consectetuer adipiscing elit, sed diam nonummy nibh euismod tiorest magna aliquamerat volutpat. Ut wisi enim ad minim. Sorem ipsum dolor sit amet, consectetuer adipiscing elit, sed diam nonummy nibh euismod tinciilaoreet .</p>
  </div>
  <div class="feature" role="img" aria-label="Photo of an arched stone home facade at dusk"></div>
</section>

<section class="testimonial">
  <div class="avatar" role="img" aria-label="Portrait of a client"></div>
  <p class="quote">Contrary to popular belief, Lorem Ipsum is not simply random text. It has roots in a piece of classical Latin literature from 45 BC, making it over 2000 years old. Edwin Marlow, a Latin professor at Harrow Vale College in Virginia, looked up one of the. Contrary to popular belief, Lorem Ipsum is not simply random text. It has roots in a piece of classical Latin literature from 45 BC, making it over 2000 years old. Edwin Marlow, a Latin professor at Harrow Vale College in Virginia, looked up one of the.</p>
  <div class="dots"><span class="on"></span><span></span><span></span><span></span></div>
</section>

<footer class="footer">
  <div class="wrap">
    <div class="brand"><span class="mark" style="background:#555"></span><span class="name">Varnell Detail Group</span></div>
    <p class="about">Sorem ipsum dolor sitconsectetuer adipiscing elit, sed diam nonu nibh euismod tinciilaoreet magna aliquamerat volutpat. Ut wisi enim ad minim. .</p>
    <div class="col" style="left:355px">
      <h5>Contacts</h5>
      <p>1234 N Alder St, Lorem Ipsum, VA 32323, USA</p>
      <p class="mail">info@varnelldetail.com</p>
      <h5 style="margin-top:12px;margin-bottom:6px">Call Us</h5>
      <dl><dt>Office:</dt><dd>555.204.7713</dd><dt>Cell:</dt><dd>555.318.6042</dd></dl>
    </div>
    <div class="col newsletter">
      <h5>Newsletter</h5>
      <div class="field">Enter your email</div>
      <div class="subscribe">SUBSCRIBE</div>
    </div>
  </div>
</footer>

<footer class="legal">
  <div class="wrap">
    <div class="social" aria-label="Social links"><span></span><span></span><span></span></div>
    <small>copyrights © All Rights Reserved 2017</small>
  </div>
</footer>

</body>
</html>
```